Security software company needs a 1 page brochure design

Looking for high-level marketing brochure, preferably one page, to give an overview of our solution. The solution should incorporate our color scheme and logo (visible on www.tovarqen.com).
Ideally, the brochure will have space for a customizable title, three primary headers, and a sidebar where bulleted features can be listed.
The three primary sections in the main area of the brochure will be "Identity Managment", "Access Control", and "Audit", and there should be space to describe these things in more detail.
It should also contain a footer, where basic company information can be displayed.
Bramwick is a security software company that helps IT organizations manage and control remote access to their sensitive information. We want to communicate that our solution is secure, professional, puts the customer in control, and provides peace of mind.
It will be presented to director level and C level buyers
Target Market(s)
Director level or C level
IT professionals
Security Professionals
Industry/Entity Type
Marketing
Look and feel

```html
<!DOCTYPE html>
<html lang="en">
<head>
<meta charset="utf-8">
<title>Bramwick – Product Overview</title>
<link rel="stylesheet" href="https://fonts.googleapis.com/css2?family=Open+Sans:ital,wght@0,400;0,600;0,700;0,800;1,700&display=swap">
<style>
:root{
  --orange:#f26522;
  --blue:#1f7fc4;
  --blue-light:#5fb3e6;
  --navy:#1b3f73;
  --ink:#2b2b2b;
  --grey:#6f6f6f;
  --rule:#cfd8e0;
  --white:#ffffff;
}
*{box-sizing:border-box;margin:0;padding:0}
html,body{width:849px;height:1200px;overflow:hidden;background:var(--white)}
body{font-family:"Open Sans",Arial,sans-serif;color:var(--ink);position:relative}
.page{position:relative;width:849px;height:1200px;overflow:hidden}

.brand{position:absolute;left:42px;top:76px;display:flex;align-items:center;gap:16px}
.brand-mark{width:52px;height:52px;border-radius:50%;background:var(--blue)}
.brand-name{font-size:46px;font-weight:800;color:var(--orange);letter-spacing:1px}

.main{position:absolute;left:30px;top:285px;width:440px}
.section{margin-bottom:26px}
.section-head{border-top:2px solid var(--rule);padding-top:16px;display:flex;align-items:center;gap:12px}
.section-head svg{flex:none}
.section-title{font-size:24px;font-weight:700;color:var(--navy);letter-spacing:.5px;line-height:1.3}
.section-body{margin-top:10px;font-size:15.5px;line-height:1.48;color:var(--ink)}

.hero{position:absolute;left:500px;top:0;width:349px;height:220px;background:linear-gradient(160deg,#d9d9d9,#8a8a8a 55%,#3c3c3c)}
.sidebar{position:absolute;left:500px;top:220px;width:349px;height:600px;background:var(--orange);padding:22px 26px 0 26px;color:var(--white)}
.sidebar h2{font-size:44px;font-weight:400;margin-bottom:16px;line-height:1.2}
.features{list-style:none}
.features li{position:relative;padding-left:22px;font-size:20px;font-weight:700;font-style:italic;line-height:1.35;margin-bottom:8px}
.features li::before{content:"";position:absolute;left:2px;top:12px;width:7px;height:7px;border-radius:50%;background:var(--white)}

.clients{position:absolute;left:500px;top:820px;width:349px;height:175px;background:var(--white);border-left:1px solid #e2e2e2}
.clients-q{position:absolute;left:24px;top:54px;font-size:25px;line-height:1.3;color:var(--grey)}
.badge{position:absolute;border-radius:3px}

.footer-wave{position:absolute;left:0;top:978px;width:849px;height:60px}
.footer{position:absolute;left:0;top:1030px;width:849px;height:170px;background:var(--orange);color:var(--white)}
.footer-label{position:absolute;left:30px;top:20px;font-size:18px;font-weight:700}
.footer-address{position:absolute;left:30px;top:60px;font-size:16px;font-weight:600;line-height:1.35}
.footer-contact{position:absolute;right:28px;top:60px;font-size:16px;font-weight:600;line-height:1.35;text-align:right}
.footer-web{margin-top:40px;display:block}
</style>
</head>
<body>
<div class="page">

  <header class="brand">
    <span class="brand-mark"></span>
    <span class="brand-name">BRAMWICK</span>
  </header>

  <div class="hero" role="img" aria-label="Close-up photo of a hand pressing a key on a computer keyboard"></div>

  <main class="main">
    <section class="section">
      <div class="section-head">
        <svg width="14" height="20" viewBox="0 0 14 20"><path d="M0 0 L14 10 L0 20 Z" fill="var(--blue)"/></svg>
        <h2 class="section-title">AUTHENTICATION</h2>
      </div>
      <p class="section-body">Lorem ipsum dolor sit amet. Sea minim dolore. Duo et takimata ipsum erat. Rebum tempor elit amet elitr dolore eos. Et consetetur eirmod erat voluptua et sit. Lorem dolor vel tation wisi aliquyam. Justo est clita molestie labore eos dolor nonumy. Autem sed sit ea. Takimata amet invidunt eros nonummy. Sit dolores volutpat sea velit magna consequat in. Eros commodo lorem nibh et eleifend. Eu sed voluptua consetetur</p>
    </section>

    <section class="section">
      <div class="section-head">
        <svg width="14" height="20" viewBox="0 0 14 20"><path d="M0 0 L14 10 L0 20 Z" fill="var(--blue)"/></svg>
        <h2 class="section-title">ACCESS CONTROL</h2>
      </div>
      <p class="section-body">Lorem ipsum dolor sit amet. Sea minim dolore. Duo et takimata ipsum erat. Rebum tempor elit amet elitr dolore eos. Et consetetur eirmod erat voluptua et sit. Lorem dolor vel tation wisi aliquyam. Justo est clita molestie labore eos dolor nonumy. Autem sed sit ea.</p>
    </section>

    <section class="section">
      <div class="section-head">
        <svg width="14" height="20" viewBox="0 0 14 20"><path d="M0 0 L14 10 L0 20 Z" fill="var(--blue)"/></svg>
        <h2 class="section-title">AUDIT</h2>
      </div>
      <p class="section-body">Lorem ipsum dolor sit amet. Sea minim dolore. Duo et takimata ipsum erat. Rebum tempor elit amet elitr dolore eos. Et consetetur eirmod erat voluptua et sit. Lorem dolor vel tation wisi aliquyam. Justo est clita molestie labore eos dolor nonumy. Autem sed sit ea.</p>
    </section>
  </main>

  <aside class="sidebar">
    <h2>Bullets</h2>
    <ul class="features">
      <li>Lorem ipsum dolor yrewsit amet. Sea refs elrokhinim dolore. Duo et taka ipsum erat.</li>
      <li>Rebum tempor elit amet elitr dolore eos. Et consetetur eirmod erat voluptua et sit.</li>
      <li>Lorem dolor vel tation wisi aliquyam. Justo est clita molestie labore eos dolor nonumy. Autem sed sit ea.</li>
      <li>Sit dolores volutpat sea velit magna consequa. Eros commodo lorem.</li>
    </ul>
  </aside>

  <section class="clients">
    <p class="clients-q">Who uses<br>Bramwick?</p>
    <span class="badge" style="left:200px;top:24px;width:50px;height:50px;background:#c8102e"></span>
    <span class="badge" style="left:262px;top:20px;width:52px;height:56px;background:#0f4d92"></span>
    <span class="badge" style="left:200px;top:86px;width:50px;height:46px;background:#2a6ebb"></span>
    <span class="badge" style="left:262px;top:90px;width:52px;height:40px;background:#6a8caf"></span>
    <span class="badge" style="left:214px;top:144px;width:100px;height:18px;background:#1d4f91"></span>
  </section>

  <svg class="footer-wave" viewBox="0 0 849 60" preserveAspectRatio="none">
    <path d="M0 36 C250 4 560 6 849 40 L849 60 L0 60 Z" fill="var(--blue-light)"/>
    <path d="M0 46 C260 16 560 18 849 50 L849 60 L0 60 Z" fill="var(--blue)"/>
  </svg>

  <footer class="footer">
    <p class="footer-label">Corporate Headquarters</p>
    <p class="footer-address">Bramwick, Inc.<br>4410 Larkspur Ridge Rd<br>Building C, Suite 310<br>Alder Falls, TX 78602</p>
    <p class="footer-contact">Phone: 512.408.2260<br>Fax 512.408.2261<span class="footer-web">www.tovarqen.com</span></p>
  </footer>

</div>
</body>
</html>
```